Price Trend Graphic for Estimates

I want to add a graphic to my estimates that shows the projected price trend of the work we are quoting to the customer. I have attached a couple ideas I was working on but they are garbage. Hopefully you can see the intent and make it look a lot better. Basically I want the customer to see a really a professional / technological graphic that will stimulate them to purchase Right Now! before the price goes up further. So maybe if the "Today's Price" looks nice and friendly and then becomes more critical and ominous as it goes forward 30 days.... 90 days.... Idea is to psychologically

Target Market(s)

Customers for our Construction business

Industry/Entity Type

Construction

Colors
0054AA
0677BA
7BADD7
CADEEF
E8F1F8
0094D4
00A9DD
6FCCEA
C7EBF8
E9F6FB
FFF300
FFF600
FEFA6F
FFFEC7
FFFEE8
F0912C
F2A743
F7CA91
FBE8D2
FDF5EE

Requirements
Must have
• nice looking graphic with upwards moving arrow and 3 price points
Nice to have
• technological / modern looking chart

```html
<!DOCTYPE html>
<html lang="en">
<head>
<meta charset="utf-8">
<title>Price Trend</title>
<link rel="stylesheet" href="https://fonts.googleapis.com/css2?family=Orbitron:wght@900&family=Audiowide&family=Sacramento&display=swap">
<style>
  :root {
    --sky: #00a9dd;
    --bright: #00b2f0;
    --white: #ffffff;
    --ink: #05070c;
    --navy-1: #0b1a2c;
    --navy-2: #16304a;
    --navy-3: #2a3a55;
  }
  html, body {
    margin: 0;
    padding: 0;
    width: 1200px;
    height: 1000px;
    overflow: hidden;
    background: var(--ink);
  }
  .price-trend {
    display: block;
    width: 1200px;
    height: 1000px;
  }
  .title {
    font-family: "Orbitron", sans-serif;
    font-weight: 900;
    fill: var(--bright);
  }
  .period {
    font-family: "Audiowide", sans-serif;
    fill: var(--sky);
  }
  .price {
    font-family: "Audiowide", sans-serif;
    fill: var(--white);
  }
  .tagline {
    font-family: "Sacramento", cursive;
    fill: var(--white);
  }
  .trend-line {
    stroke: var(--bright);
    stroke-width: 8;
    fill: none;
  }
  .trend-point {
    fill: var(--bright);
  }
</style>
</head>
<body>
<svg class="price-trend" viewBox="0 0 1200 1000" xmlns="http://www.w3.org/2000/svg">
  <defs>
    <radialGradient id="hud-glow" cx="0.6" cy="0.4" r="0.8">
      <stop offset="0" stop-color="var(--navy-3)"/>
      <stop offset="0.55" stop-color="var(--navy-2)"/>
      <stop offset="1" stop-color="var(--navy-1)"/>
    </radialGradient>
    <linearGradient id="footer-fade" x1="0" y1="0" x2="0" y2="1">
      <stop offset="0" stop-color="var(--ink)" stop-opacity="0"/>
      <stop offset="1" stop-color="var(--ink)"/>
    </linearGradient>
  </defs>

  <rect class="backdrop" x="0" y="0" width="1200" height="860" fill="url(#hud-glow)"
        role="img" aria-label="Dark blue technology dashboard backdrop with charts, icons, world map and a hand touching a screen"/>
  <rect class="footer-band" x="0" y="820" width="1200" height="180" fill="url(#footer-fade)"/>
  <rect x="0" y="860" width="1200" height="140" fill="var(--ink)"/>

  <text class="title" x="54" y="186" font-size="112" textLength="1090" lengthAdjust="spacingAndGlyphs">PRICE TREND</text>

  <polyline class="trend-line" points="42,760 646,596 1072,280"/>
  <circle class="trend-point" cx="42" cy="760" r="40"/>
  <circle class="trend-point" cx="646" cy="596" r="60"/>
  <circle class="trend-point" cx="1072" cy="280" r="76"/>

  <text class="period" x="18" y="692" font-size="34" textLength="176" lengthAdjust="spacingAndGlyphs">TODAY</text>
  <text class="price" x="16" y="872" font-size="34" textLength="238" lengthAdjust="spacingAndGlyphs">$6,500.00</text>

  <text class="period" x="514" y="525" font-size="36" textLength="226" lengthAdjust="spacingAndGlyphs">30 DAYS</text>
  <text class="price" x="540" y="701" font-size="36" textLength="238" lengthAdjust="spacingAndGlyphs">$7,280.00</text>

  <text class="period" x="762" y="321" font-size="36" textLength="224" lengthAdjust="spacingAndGlyphs">60 DAYS</text>
  <text class="price" x="960" y="407" font-size="36" textLength="232" lengthAdjust="spacingAndGlyphs">$7,460.00</text>

  <text class="tagline" x="302" y="932" font-size="118" textLength="826" lengthAdjust="spacingAndGlyphs">Signup today for huge savings!</text>
</svg>
</body>
</html>
```